Business Card Needed - Web Design (Promo Card)

Our web design company is currently offering a promo for new web sites.
$195 Setup
$95/mo
Month to Month, No Cancellation Fees
This is for a full web design for any company. We're looking to create promotional cards the size of business cards to promote this offer.
The cards should be very eye catching, could be cartoony, I really am open to any type of design. Our current business cards feature all our products and though very professional they are to detailed.
Here is our logo (doesn't necessary have to be included):
http://www.velmorapix.com/images/lg-logo.png
Here are some card ideas I like.

```html
<!DOCTYPE html>
<html lang="en">
<head>
<meta charset="utf-8">
<title>Velmorapix – Website Promotion Card</title>
<link rel="stylesheet" href="https://fonts.googleapis.com/css2?family=Arimo:wght@400;700&display=swap">
<style>
  :root {
    --page-bg: #e8e5e0;
    --card-white: #ffffff;
    --deep-blue: #3a70b2;
    --sky-blue: #8db8ea;
    --promo-orange: #f0860e;
    --ink: #111111;
  }
  html, body {
    margin: 0;
    width: 1200px;
    height: 900px;
    overflow: hidden;
    background: var(--page-bg);
  }
  .promo-card {
    position: absolute;
    left: 97px;
    top: 160px;
    width: 1006px;
    height: 580px;
    background: var(--card-white);
  }
  .promo-card svg { display: block; }
  .txt { font-family: "Arimo", Arial, sans-serif; font-weight: 700; }
  .price { fill: var(--card-white); font-size: 90px; }
  .price-unit { fill: var(--card-white); font-size: 25px; font-weight: 400; }
  .price-only { fill: var(--promo-orange); font-size: 56px; }
  .headline {
    fill: var(--promo-orange);
    font-size: 76px;
    stroke: var(--card-white);
    stroke-width: 8px;
    paint-order: stroke;
    stroke-linejoin: round;
  }
  .terms { fill: var(--ink); font-size: 46px; }
  .terms-small { font-size: 31px; }
  .tagline-light { fill: var(--card-white); font-size: 54px; }
  .tagline-bold { fill: var(--card-white); font-size: 62px; }
  .brand-name { fill: var(--deep-blue); font-size: 44px; }
  .brand-dot { fill: var(--deep-blue); }
  .stop-deep { stop-color: var(--deep-blue); }
  .stop-sky { stop-color: var(--sky-blue); }
  .stop-white { stop-color: var(--card-white); }
</style>
</head>
<body>
  <div class="promo-card">
    <svg width="1006" height="580" viewBox="0 0 1006 580" xmlns="http://www.w3.org/2000/svg">
      <defs>
        <radialGradient id="deep-field" gradientUnits="userSpaceOnUse" cx="0" cy="0" r="500" gradientTransform="scale(1 0.94)">
          <stop offset="0.93" class="stop-deep"/>
          <stop offset="1" class="stop-deep" stop-opacity="0"/>
        </radialGradient>
        <radialGradient id="sky-field" gradientUnits="userSpaceOnUse" cx="1006" cy="580" r="600">
          <stop offset="0.78" class="stop-sky"/>
          <stop offset="1" class="stop-sky" stop-opacity="0"/>
        </radialGradient>
      </defs>

      <g role="img" aria-label="Paint splash backdrop in deep blue and sky blue">
        <rect width="1006" height="580" fill="url(#sky-field)"/>
        <rect width="1006" height="580" fill="url(#deep-field)"/>
      </g>

      <!-- pricing -->
      <text class="txt price" x="25" y="113" textLength="233" lengthAdjust="spacingAndGlyphs">$195</text>
      <text class="txt price-unit" x="270" y="112" textLength="93" lengthAdjust="spacingAndGlyphs">SETUP</text>
      <text class="txt price" x="25" y="220" textLength="175" lengthAdjust="spacingAndGlyphs">$95</text>
      <text class="txt price-unit" x="215" y="218" textLength="168" lengthAdjust="spacingAndGlyphs">PER MONTH</text>
      <text class="txt price-only" x="27" y="290" textLength="183" lengthAdjust="spacingAndGlyphs">ONLY</text>

      <!-- headline -->
      <text class="txt headline" x="628" y="82" textLength="357" lengthAdjust="spacingAndGlyphs">WEBSITE</text>
      <text class="txt headline" x="498" y="167" textLength="487" lengthAdjust="spacingAndGlyphs">PROMOTION</text>

      <!-- terms -->
      <text class="txt terms" x="463" y="301" textLength="484" lengthAdjust="spacingAndGlyphs">MONTH <tspan class="terms-small">TO</tspan> MONTH</text>
      <text class="txt terms" x="463" y="357" textLength="482" lengthAdjust="spacingAndGlyphs">NO <tspan class="terms-small">CANCELLATION FEES</tspan></text>

      <!-- tagline -->
      <text class="txt tagline-light" x="651" y="483" textLength="332" lengthAdjust="spacingAndGlyphs">affordable</text>
      <text class="txt tagline-bold" x="558" y="555" textLength="422" lengthAdjust="spacingAndGlyphs">WEB DESIGN</text>

      <!-- brand -->
      <circle class="brand-dot" cx="45" cy="522" r="18"/>
      <text class="txt brand-name" x="75" y="537">Velmorapix</text>
    </svg>
  </div>
</body>
</html>
```